Social Search engine to end child poverty

Velbrix.org is a search engine based in Houston, that donates 50% or more of its profits to nonprofit organizations that focus on ending child poverty. We consider itself a social business, claims to support full financial transparency,protect the privacy of its users;

Velbrix shows advertisements next to its search results, and is paid by partners every time a user is directed to an advertiser via a sponsored link.
We are committed to becoming a privacy friendly search engine. Searches will be encrypted, not stored permanently, and data will not not sold to third party advertisers.
Like www.quandu.org Every search done by website visitor will generate a GRINTO that will be stored in his wallet. Then the visitor can donate these GRINTOS to The idea behind is evry donation will put a SMILE back on a child face

The search engine will partner with foundations/associations/NGOs that will be able to propose crowdfunding campaigns on the landing page

The beta test will be done with african children. So the landing page should show faces of happiness, joy, children

Please find attached inspirational ideas in the PDF file

Target Market(s)

NGO, Foundation, association, donators based in USA

Industry/Entity Type

Charity

Number of Pages Required

5+ page

Colors
33a6d7
fbed22
f04a50
a54499
f78d1f
add136

Requirements
Must have
• Landing page
• 0- Number of GRINTOS collected worlwide/number of projects funded
• 1- explaining how it works and
• 2- samples of fundable projects
• 3- Become partner
• Search results
• 1- Sponsored results should be differentiated
• 2- The search page should advertise initiative pr people that acts in the world to end child poverty.
• 3 It should also provide quizzes with some metrics/figures on child poverty
• Under the search engine bar should be "News" "Videos

```html
<!DOCTYPE html>
<html lang="en">
<head>
<meta charset="utf-8">
<title>Velbrix — Give Meaning to your Searches</title>
<link href="https://fonts.googleapis.com/css2?family=Nunito:wght@700;800;900&family=Nunito+Sans:wght@300;400;600;700;800&display=swap" rel="stylesheet">
<style>
:root{
  --blue:#2d8fd5;
  --sky:#33a6d7;
  --yellow:#fbed22;
  --red:#e8304f;
  --coral:#f04a50;
  --purple:#a54499;
  --orange:#f47a1f;
  --green:#a2c92e;
  --ink:#2b2b2b;
  --text:#4a4a4a;
  --soil:#3b2a24;
  --mist:#eeeeef;
  --night:#232323;
  --white:#ffffff;
}
*{box-sizing:border-box;margin:0;padding:0}
html,body{width:1200px;height:4297px;overflow:hidden}
body{position:relative;background:var(--white);font-family:"Nunito Sans",Arial,sans-serif;color:var(--text)}
.abs{position:absolute}
.photo{background:linear-gradient(135deg,#6b4330 0%,#a5673f 40%,#3c2a22 100%)}

/* hero */
.hero{left:0;top:0;width:1200px;height:651px;overflow:hidden;
  background:linear-gradient(110deg,#7a3b2a 0%,#b4392f 18%,#3f5fa0 32%,#6d4a34 55%,#5a3a29 75%,#2f251f 100%)}
.hero-shade{position:absolute;inset:0;background:rgba(30,18,12,.38)}
.brand{left:75px;top:38px;font-family:"Nunito",sans-serif;font-weight:800;font-size:56px;color:var(--white);letter-spacing:.5px}
.menu{left:1093px;top:68px;width:34px}
.menu span{display:block;height:5px;background:var(--white);border-radius:2px;margin-bottom:6px}
.hero-title{left:0;width:1200px;top:236px;text-align:center;font-family:"Nunito",sans-serif;font-weight:900;font-size:54px;color:var(--white);letter-spacing:1px}
.hero-sub{left:250px;width:700px;top:310px;text-align:center;font-size:28px;line-height:37px;color:var(--white);font-weight:400}
.hero-domain{left:0;width:1200px;top:380px;text-align:center;font-family:"Nunito",sans-serif;font-weight:900;font-size:64px;color:var(--white)}
.hero-search{left:254px;top:477px;width:692px;height:54px;border-radius:27px;background:var(--white);display:flex;align-items:center;justify-content:space-between;padding:0 24px 0 22px;font-size:20px;color:var(--ink)}

/* about */
.about-card{left:75px;top:651px;width:1052px;height:476px;background:var(--white);
  clip-path:polygon(0 0,100% 0,100% 100%,0 67%);}
.about-title{left:120px;top:690px;font-size:46px;font-weight:300;color:var(--ink);letter-spacing:1px}
.about-text{left:122px;top:760px;width:570px;font-size:16.5px;line-height:32.5px;color:var(--ink)}
.btn-video{left:120px;top:876px;width:227px;height:42px;border-radius:21px;background:var(--red);color:var(--white);font-size:18px;display:flex;align-items:center;justify-content:center}
.about-art{left:712px;top:700px;width:392px;height:292px;border-radius:120px 40px 40px 140px;background:linear-gradient(160deg,#e2e3f3,#c9cbe6)}

/* sections */
.section-title{left:0;width:1200px;text-align:center;font-size:46px;font-weight:300;color:var(--ink);letter-spacing:1px}
.section-title.light{color:var(--white)}
.work-card{top:1289px;width:330px;height:355px;border-radius:6px;color:var(--white);text-align:center;padding:40px 22px 0}
.work-card svg{display:block;margin:0 auto 20px}
.work-card h3{font-size:23px;font-weight:600;margin-bottom:10px}
.work-card p{font-size:16.5px;line-height:27px;opacity:.92}
.c-orange{background:var(--orange)}
.c-red{background:var(--red)}
.c-green{background:var(--green)}
.c-blue{background:var(--blue)}

.stat{top:1819px;width:242px;height:102px;background:var(--white);border-radius:4px;display:flex;align-items:center;padding-left:28px;gap:18px}
.stat b{font-family:"Nunito",sans-serif;font-size:48px;font-weight:900;color:var(--red);letter-spacing:2px}
.stat span{font-size:21px;line-height:28px;color:var(--ink)}
.stat span strong{font-weight:700}

.sub-note{left:0;width:1200px;top:2101px;text-align:center;font-size:17px;color:var(--purple)}
.cat{top:2163px;width:242px;height:99px;border-radius:5px;color:var(--white);display:flex;flex-direction:column;align-items:center;justify-content:center;gap:8px;font-size:17px;font-weight:800;letter-spacing:.5px}

.project{width:330px;height:415px;background:var(--white);border-radius:6px;box-shadow:0 2px 10px rgba(0,0,0,.12);padding:15px}
.project .pic{width:300px;height:179px;border-radius:3px}
.project h4{text-align:center;margin-top:16px;font-size:23px;font-weight:600;color:var(--blue)}
.project p{text-align:center;margin-top:8px;font-size:16.5px;line-height:27px;color:var(--ink)}
.project .meta{position:absolute;left:15px;right:15px;bottom:22px;border-top:1px solid #e2e2e2;padding-top:22px;display:flex;align-items:center;justify-content:space-between}
.bar{width:228px;height:9px;border-radius:5px;background:#e3e3e3;overflow:hidden}
.bar i{display:block;width:40%;height:100%;background:var(--green)}
.price{font-size:20px;color:var(--red);font-weight:600}

.partner{top:3358px;width:242px;height:103px;background:var(--white);border-radius:4px;box-shadow:0 2px 10px rgba(0,0,0,.1);display:flex;align-items:center;justify-content:center;gap:10px;font-size:30px;font-weight:700;color:var(--ink)}
.partner i{width:24px;height:24px;border-radius:50%;display:block}

/* news */
.news{left:75px;top:3541px;width:1052px;height:591px;background:var(--blue);border-radius:5px}
.news-tabs{left:0;width:1200px;top:3578px;text-align:center;font-size:46px;font-weight:300;color:var(--white);letter-spacing:1px}
.news-tabs .on{color:var(--yellow);text-decoration:underline;text-underline-offset:7px;text-decoration-thickness:2px}
.news-tabs .sep{margin:0 22px}
.news-search{left:434px;top:3677px;width:332px;height:40px;border-radius:20px;background:var(--white);display:flex;align-items:center;justify-content:space-between;padding:0 18px 0 22px;font-size:14px;color:var(--ink)}
.news-item{top:3754px;width:282px}
.news-item .pic{height:183px;border-radius:3px}
.news-item h5{margin-top:18px;font-size:23px;font-weight:600;color:var(--yellow);white-space:nowrap}
.news-item p{margin-top:6px;font-size:16.5px;line-height:27px;color:var(--white)}

.footer{left:0;top:3981px;width:1200px;height:316px;background:var(--night)}
.copy{left:0;width:1200px;top:4188px;text-align:center;font-size:14px;color:var(--white)}
.social{left:0;width:1200px;top:4227px;display:flex;justify-content:center;gap:20px}
.social i{width:22px;height:22px;border-radius:50%;background:var(--white);display:block}
</style>
</head>
<body>

<!-- background shapes -->
<svg class="abs" style="left:0;top:0" width="1200" height="4297" aria-hidden="true">
  <polygon points="0,651 1200,651 1200,690 0,1150" fill="#3b2a24"/>
  <polygon points="0,1218 1200,1678 1200,1986 0,1986" fill="#2d8fd5"/>
  <polygon points="1200,2860 1200,3652 0,3652 0,3340" fill="#eeeeef"/>
</svg>

<header class="abs hero" role="img" aria-label="Photo of a smiling child at a colourful playground">
  <div class="hero-shade"></div>
</header>
<div class="abs brand">Velbrix</div>
<div class="abs menu" aria-label="Menu"><span></span><span></span><span></span></div>
<h1 class="abs hero-title">Give Meaning to your Searches</h1>
<p class="abs hero-sub">With Velbrix, your searches funds programs targeting disadvantaged children.</p>
<div class="abs hero-domain">velbrix.org</div>
<div class="abs hero-search">
  <span>Search</span>
  <svg width="26" height="26" viewBox="0 0 24 24" fill="none" stroke="#222" stroke-width="3"><circle cx="10" cy="10" r="7"/><line x1="15" y1="15" x2="22" y2="22" stroke-linecap="round"/></svg>
</div>

<!-- about -->
<section class="abs about-card" style="box-shadow:0 4px 14px rgba(0,0,0,.15)"></section>
<h2 class="abs about-title">About Velbrix</h2>
<p class="abs about-text">Lorem ipsum dolor sit amet, consectetur adipiscing elit. Morbi id felis libero. Nullam ultrices risus feugiat sodales fermentum. Etiam euismod quis odio in eleifend. Mauris euismod scelerisque tincidunt.</p>
<div class="abs btn-video">Video Presentation</div>
<div class="abs about-art" role="img" aria-label="Illustration of children playing jump rope"></div>

<!-- how it works -->
<h2 class="abs section-title" style="top:1172px">How it Works</h2>
<div class="abs work-card c-orange" style="left:75px">
  <svg width="96" height="80" viewBox="0 0 96 80" fill="none" stroke="#fff" stroke-width="3"><circle cx="30" cy="28" r="16"/><circle cx="66" cy="28" r="16"/><path d="M6 78c0-16 10-26 24-26s24 10 24 26"/><path d="M42 78c0-16 10-26 24-26s24 10 24 26"/></svg>
  <h3>Mauris Euismod</h3>
  <p>Donec facilisis arcu sit amet nisi rutrum, eu dignissim justo sagittis euismod scelerisque facilisis mauris eget dolor placerat ultrices.</p>
</div>
<div class="abs work-card c-red" style="left:436px">
  <svg width="96" height="80" viewBox="0 0 96 80" fill="none" stroke="#fff" stroke-width="3"><path d="M48 74 18 44a16 16 0 0 1 30-18 16 16 0 0 1 30 18z"/></svg>
  <h3>Mauris Euismod</h3>
  <p>Donec facilisis arcu sit amet nisi rutrum, eu dignissim justo sagittis euismod scelerisque facilisis mauris eget dolor placerat ultrices.</p>
</div>
<div class="abs work-card c-green" style="left:796px">
  <svg width="96" height="80" viewBox="0 0 96 80" fill="none" stroke="#fff" stroke-width="3"><path d="M48 40 32 24a9 9 0 0 1 16-10 9 9 0 0 1 16 10z"/><path d="M10 60h20l14 8h24l18-14"/><path d="M30 60l14-8h14"/></svg>
  <h3>Mauris Euismod</h3>
  <p>Donec facilisis arcu sit amet nisi rutrum, eu dignissim justo sagittis euismod scelerisque facilisis mauris eget dolor placerat ultrices.</p>
</div>

<!-- fundable projects -->
<h2 class="abs section-title light" style="top:1732px">Fundable Projects</h2>
<div class="abs stat" style="left:75px"><b>21</b><span><strong>Donec</strong><br>Sollicitudin</span></div>
<div class="abs stat" style="left:345px"><b>15</b><span><strong>Donec</strong><br>Sollicitudin</span></div>
<div class="abs stat" style="left:616px"><b>62</b><span><strong>Donec</strong><br>Sollicitudin</span></div>
<div class="abs stat" style="left:885px"><b>35</b><span><strong>Donec</strong><br>Sollicitudin</span></div>

<!-- project to finance -->
<h2 class="abs section-title" style="top:2038px">Project to Finance</h2>
<p class="abs sub-note">You shall finance one project or more.</p>
<div class="abs cat c-green" style="left:75px">
  <svg width="32" height="28" viewBox="0 0 32 28"><path d="M16 27 3 14A7.5 7.5 0 0 1 16 5a7.5 7.5 0 0 1 13 9z" fill="#fff"/></svg>Environment</div>
<div class="abs cat c-red" style="left:345px">
  <svg width="34" height="28" viewBox="0 0 34 28" fill="#fff"><circle cx="17" cy="8" r="6"/><circle cx="6" cy="11" r="4"/><circle cx="28" cy="11" r="4"/><path d="M6 28a11 11 0 0 1 22 0z"/><path d="M0 26a6 6 0 0 1 8-6l-1 6zM34 26a6 6 0 0 0-8-6l1 6z"/></svg>Social</div>
<div class="abs cat c-orange" style="left:616px">
  <svg width="26" height="30" viewBox="0 0 26 30" fill="none" stroke="#fff" stroke-width="2.5"><rect x="3" y="2" width="20" height="27"/><path d="M13 6v8M9 10h8M8 18h3M15 18h3M8 23h3M15 23h3"/></svg>Health</div>
<div class="abs cat c-blue" style="left:885px">
  <svg width="36" height="26" viewBox="0 0 36 26" fill="#fff"><path d="M18 2 0 10l18 8 18-8z"/><path d="M7 14v7c4 4 18 4 22 0v-7l-11 5z"/><rect x="32" y="10" width="2" height="10"/></svg>Education</div>

<article class="abs project" style="left:75px;top:2305px"><div class="pic photo" role="img" aria-label="Photo of children playing together outdoors"></div><h4>Project Heading</h4><p>Donec facilisis arcu sit amet nisi rutrum, eu dignissim justo sagittis euismod scelerisque.</p><div class="meta"><div class="bar"><i></i></div><span class="price">$250</span></div></article>
<article class="abs project" style="left:434px;top:2305px"><div class="pic photo" role="img" aria-label="Photo of a group of smiling children indoors"></div><h4>Project Heading</h4><p>Donec facilisis arcu sit amet nisi rutrum, eu dignissim justo sagittis euismod scelerisque.</p><div class="meta"><div class="bar"><i></i></div><span class="price">$250</span></div></article>
<article class="abs project" style="left:796px;top:2305px"><div class="pic" style="background:linear-gradient(135deg,#2f4f7a,#b3343c 50%,#3a2c28)" role="img" aria-label="Photo of schoolchildren with colourful backpacks"></div><h4>Project Heading</h4><p>Donec facilisis arcu sit amet nisi rutrum, eu dignissim justo sagittis euismod scelerisque.</p><div class="meta"><div class="bar"><i></i></div><span class="price">$250</span></div></article>
<article class="abs project" style="left:75px;top:2749px"><div class="pic" style="background:linear-gradient(135deg,#3a2620,#a8443a 55%,#2a1c18)" role="img" aria-label="Photo of children studying at a desk"></div><h4>Project Heading</h4><p>Donec facilisis arcu sit amet nisi rutrum, eu dignissim justo sagittis euismod scelerisque.</p><div class="meta"><div class="bar"><i></i></div><span class="price">$250</span></div></article>
<article class="abs project" style="left:434px;top:2749px"><div class="pic" style="background:linear-gradient(135deg,#6b4a36,#b07a55 50%,#7c8a96)" role="img" aria-label="Photo of a joyful girl smiling"></div><h4>Project Heading</h4><p>Donec facilisis arcu sit amet nisi rutrum, eu dignissim justo sagittis euismod scelerisque.</p><div class="meta"><div class="bar"><i></i></div><span class="price">$250</span></div></article>
<article class="abs project" style="left:796px;top:2749px"><div class="pic" style="background:linear-gradient(135deg,#2a1d17,#6a4534 50%,#3a2a22)" role="img" aria-label="Photo of laughing boys close together"></div><h4>Project Heading</h4><p>Donec facilisis arcu sit amet nisi rutrum, eu dignissim justo sagittis euismod scelerisque.</p><div class="meta"><div class="bar"><i></i></div><span class="price">$250</span></div></article>

<!-- partners -->
<h2 class="abs section-title" style="top:3270px">Become Partner</h2>
<div class="abs partner" style="left:75px"><i style="background:var(--orange)"></i>Norvale</div>
<div class="abs partner" style="left:345px"><i style="background:var(--yellow)"></i>Quintly</div>
<div class="abs partner" style="left:616px"><i style="background:var(--coral)"></i>Brisko</div>
<div class="abs partner" style="left:885px"><i style="background:var(--blue)"></i>Aldera</div>

<!-- footer band behind news -->
<footer class="abs footer"></footer>

<!-- news -->
<section class="abs news"></section>
<div class="abs news-tabs"><span class="on">News</span><span class="sep">|</span>Videos</div>
<div class="abs news-search"><span>Search...</span>
  <svg width="16" height="16" viewBox="0 0 24 24" fill="none" stroke="#e8304f" stroke-width="3"><circle cx="10" cy="10" r="7"/><line x1="15" y1="15" x2="22" y2="22" stroke-linecap="round"/></svg></div>
<div class="abs news-item" style="left:137px"><div class="pic photo" role="img" aria-label="Photo of cheerful children crowding together"></div><h5>Curabitur efficitur libero</h5><p>Donec facilisis arcu sit amet nisi rutrum, eu dignissim justo sagittis euismod scelerisque.</p></div>
<div class="abs news-item" style="left:459px"><div class="pic" style="background:linear-gradient(135deg,#8a4a34,#c97a52 50%,#5a3a2a)" role="img" aria-label="Photo of children sitting outside a village home"></div><h5>Curabitur efficitur libero</h5><p>Donec facilisis arcu sit amet nisi rutrum, eu dignissim justo sagittis euismod scelerisque.</p></div>
<div class="abs news-item" style="left:783px"><div class="pic" style="background:linear-gradient(135deg,#5a4038,#9c5a48 45%,#3c4f7a)" role="img" aria-label="Photo of a family group sitting together"></div><h5>Curabitur efficitur libero</h5><p>Donec facilisis arcu sit amet nisi rutrum, eu dignissim justo sagittis euismod scelerisque.</p></div>

<p class="abs copy">Copyright © 2019, Company Name All Right reserved</p>
<div class="abs social" aria-label="Social links"><i></i><i></i><i></i><i></i><i></i></div>

</body>
</html>
```